Tavlune

I'd like new business card design options. I'll need to provide updated contact info although after the deign is complete. We are in IT, specifically in the data backup, archiving and disaster recovery verticals.

Business

```html
<!DOCTYPE html>
<html lang="en">
<head>
<meta charset="utf-8">
<title>Tavlune business cards</title>
<link rel="stylesheet" href="https://fonts.googleapis.com/css2?family=Arimo:wght@400;700&display=swap">
<style>
  :root {
    --page: #e9ecef;
    --white: #ffffff;
    --paper: #f5f6f7;
    --blue-deep: #0b5fae;
    --blue-mid: #1a7cc9;
    --blue-light: #2ea3dd;
    --text-dark: #3c4650;
    --text-grey: #5d6670;
  }
  * { margin: 0; padding: 0; box-sizing: border-box; }
  html, body { width: 1200px; height: 1023px; overflow: hidden; }
  body {
    background: var(--page);
    font-family: "Arimo", Arial, sans-serif;
    position: relative;
  }
  .card {
    position: absolute;
    width: 580px;
    height: 332px;
    border-radius: 22px;
    overflow: hidden;
    box-shadow: 0 10px 28px rgba(0, 0, 0, 0.18);
  }

  /* Brand name */
  .brand {
    position: absolute;
    display: flex;
    align-items: center;
    gap: 16px;
  }
  .brand-dot {
    width: 56px;
    height: 56px;
    border-radius: 50%;
    flex: none;
  }
  .brand-name {
    font-weight: 700;
    font-size: 44px;
    letter-spacing: 9px;
    line-height: 1;
  }

  /* Front */
  .card-front {
    left: 80px;
    top: 120px;
    background: linear-gradient(180deg, var(--white), var(--paper));
  }
  .front-brand { left: 40px; top: 50px; }
  .front-brand .brand-dot { background: var(--blue-light); }
  .front-brand .brand-name { color: var(--blue-deep); }
  .front-band { position: absolute; left: 0; top: 148px; width: 580px; height: 58px; }
  .holder {
    position: absolute;
    left: 40px;
    top: 157px;
    color: var(--white);
  }
  .holder-name { font-weight: 700; font-size: 20px; letter-spacing: 0.3px; }
  .holder-role { font-size: 14px; letter-spacing: 0.5px; margin-top: 3px; }
  .contacts {
    position: absolute;
    left: 40px;
    top: 228px;
    list-style: none;
    font-size: 14px;
    color: var(--text-dark);
    line-height: 19px;
  }
  .contacts li { display: flex; align-items: center; gap: 8px; }
  .contacts svg { width: 12px; height: 12px; fill: var(--blue-deep); flex: none; }
  .address {
    position: absolute;
    right: 40px;
    top: 232px;
    font-size: 15px;
    font-style: normal;
    line-height: 21px;
    color: var(--text-grey);
    text-align: right;
  }
  .front-edge {
    position: absolute;
    left: 0; bottom: 0;
    width: 100%; height: 8px;
    background: var(--blue-mid);
  }

  /* Back */
  .card-back {
    left: 540px;
    top: 560px;
    background: linear-gradient(160deg, var(--blue-light) 0%, var(--blue-mid) 55%, var(--blue-deep) 100%);
    color: var(--white);
  }
  .back-brand { left: 150px; top: 64px; }
  .back-brand .brand-dot { background: var(--white); opacity: 0.9; }
  .back-brand .brand-name { color: var(--white); }
  .providers {
    position: absolute;
    left: 0; right: 0;
    top: 176px;
    text-align: center;
    font-size: 15px;
    line-height: 21px;
    letter-spacing: 0.5px;
  }
  .services {
    position: absolute;
    left: 0; right: 0;
    bottom: 32px;
    text-align: center;
    font-size: 13.5px;
    letter-spacing: 0.6px;
  }
</style>
</head>
<body>

<section class="card card-front" aria-label="Business card front">
  <div class="brand front-brand">
    <span class="brand-dot"></span>
    <div class="brand-name">TAVLUNE</div>
  </div>

  <svg class="front-band" viewBox="0 0 580 58" aria-hidden="true">
    <rect x="0" y="0" width="580" height="58" fill="#0b5fae"/>
    <polygon points="470,0 580,0 580,58 450,58" fill="#2ea3dd"/>
  </svg>

  <div class="holder">
    <div class="holder-name">MARCUS L. HENDRY, Ph.D.</div>
    <div class="holder-role">PRESIDENT, CTO</div>
  </div>

  <ul class="contacts">
    <li><svg viewBox="0 0 12 12"><path d="M2.5 0.5 4.5 3 3.4 4.3a7 7 0 0 0 4.3 4.3L9 7.5l2.5 2-1.4 2C5 11.3 0.7 7 0.5 1.9z"/></svg>800.555.0142</li>
    <li><svg viewBox="0 0 12 12"><rect x="2" y="0.5" width="8" height="4"/><rect x="0.5" y="5" width="11" height="6.5" rx="1"/></svg>928.555.0187</li>
    <li><svg viewBox="0 0 12 12"><path d="M0.5 2h11v8h-11z M1.5 3l4.5 3.5L10.5 3" fill="none" stroke="#0b5fae" stroke-width="1.3"/></svg>marcus.hendry@tavlune.com</li>
    <li><svg viewBox="0 0 12 12"><circle cx="6" cy="6" r="5.5"/><path d="M0.5 6h11M6 0.5v11" stroke="#ffffff" stroke-width="0.8"/></svg>www.tavlune.com</li>
  </ul>

  <address class="address">
    240 North Elm Avenue<br>
    Fairview, Texas 75002
  </address>

  <div class="front-edge"></div>
</section>

<section class="card card-back" aria-label="Business card back">
  <div class="brand back-brand">
    <span class="brand-dot"></span>
    <div class="brand-name">TAVLUNE</div>
  </div>

  <p class="providers">
    PROVIDERS OF<br>
    VaultPoint&trade; and CoreKeep&trade;
  </p>

  <p class="services">ONLINE PC BACKUP | CONTINUOUS SERVER BACKUP | DATA ARCHIVING</p>
</section>

</body>
</html>
```